Tavenorix - world unique technology for better life - please let them know who am i at first sight

We need a new business card for company which is a provider of unique crystal based technology suitable for all living being. For more information and final design you can use our brochure (our colours are black and blue from brochure).
We use Verdana font

Industry/Entity Type

Business

Contact Information for Business Card

regular dimension

Font styles to use
Other font styles liked:
• Verdana

Requirements
Must have
• Logo
• name
• function/position
• phone
• mobile
• e-mail
• adress
Nice to have
• inovative design (technology directed)

```html
<!DOCTYPE html>
<html lang="en">
<head>
<meta charset="utf-8">
<title>Tavenorix Business Card</title>
<link rel="stylesheet" href="https://fonts.googleapis.com/css2?family=Noto+Sans:wght@300;400;600&display=swap">
<style>
  :root {
    --blue: #29abe2;
    --grey: #a7a9ac;
    --paper: #f4f5f6;
    --white: #ffffff;
    --ink: #3a3a3c;
    --backdrop: #e6e7e9;
  }
  * { margin: 0; padding: 0; box-sizing: border-box; }
  html, body { width: 1200px; height: 828px; overflow: hidden; }
  body {
    background: var(--backdrop);
    font-family: "Noto Sans", Verdana, sans-serif;
    position: relative;
  }
  .card {
    position: absolute;
    left: 270px;
    width: 660px;
    height: 377px;
    overflow: hidden;
    box-shadow: 0 4px 14px rgba(0,0,0,0.15);
    background: var(--paper);
  }
  .card--front { top: 22px; }
  .card--back { top: 429px; }
  .card__art { position: absolute; inset: 0; width: 100%; height: 100%; }

  .brand {
    position: absolute;
    display: flex;
    align-items: center;
    gap: 12px;
  }
  .brand__mark {
    width: 48px; height: 48px;
    border-radius: 50%;
  }
  .brand__name {
    font-weight: 300;
    font-size: 34px;
    letter-spacing: 2px;
    text-transform: uppercase;
    white-space: nowrap;
  }
  .card--front .brand { left: 64px; top: 152px; }
  .card--front .brand__mark { background: var(--white); }
  .card--front .brand__name { color: var(--white); }
  .card--back .brand { left: 70px; top: 154px; }
  .card--back .brand__mark { background: var(--blue); }
  .card--back .brand__name { color: var(--blue); }

  .person { position: absolute; left: 70px; top: 262px; }
  .person__name {
    color: var(--blue);
    font-size: 22px;
    font-weight: 400;
    text-transform: uppercase;
    letter-spacing: 1px;
  }
  .person__role { color: var(--ink); font-size: 14px; margin-top: 2px; }

  .contacts {
    position: absolute;
    left: 470px;
    top: 128px;
    list-style: none;
    color: var(--white);
    font-size: 11px;
  }
  .contacts li { display: flex; align-items: center; gap: 8px; height: 24px; white-space: nowrap; }
  .contacts svg { width: 14px; height: 14px; flex: none; }
</style>
</head>
<body>

<section class="card card--front" aria-label="Card front">
  <svg class="card__art" viewBox="0 0 660 377" preserveAspectRatio="none" aria-hidden="true">
    <rect width="660" height="377" fill="var(--blue)"/>
    <path d="M660,0 L470,0 C440,150 300,300 140,377 L660,377 Z" fill="var(--grey)"/>
    <path d="M660,0 L500,0 C470,160 330,310 180,377 L660,377 Z" fill="var(--paper)"/>
    <path d="M560,0 L590,0 C560,110 520,180 470,240 C510,170 540,90 560,0 Z" fill="var(--grey)"/>
    <path d="M620,0 L650,0 C610,100 580,160 540,210 C580,140 605,80 620,0 Z" fill="var(--blue)"/>
  </svg>
  <div class="brand">
    <span class="brand__mark"></span>
    <span class="brand__name">Tavenorix</span>
  </div>
</section>

<section class="card card--back" aria-label="Card back">
  <svg class="card__art" viewBox="0 0 660 377" preserveAspectRatio="none" aria-hidden="true">
    <rect width="660" height="377" fill="var(--paper)"/>
    <path d="M660,0 L430,0 C410,150 340,280 240,377 L660,377 Z" fill="var(--grey)"/>
    <path d="M660,0 L470,0 C450,150 390,280 300,377 L660,377 Z" fill="var(--blue)"/>
    <path d="M365,0 L395,0 C385,60 368,100 340,130 C358,90 364,50 365,0 Z" fill="var(--grey)"/>
    <path d="M410,0 L428,0 C422,50 410,85 392,110 C402,75 408,40 410,0 Z" fill="var(--blue)"/>
    <path d="M605,0 L628,0 C615,45 598,78 572,105 C590,70 600,40 605,0 Z" fill="var(--paper)"/>
    <path d="M0,377 L0,362 C80,360 160,352 230,340 C180,360 120,372 60,377 Z" fill="var(--blue)"/>
  </svg>
  <div class="brand">
    <span class="brand__mark"></span>
    <span class="brand__name">Tavenorix</span>
  </div>
  <div class="person">
    <p class="person__name">Marek Olsen</p>
    <p class="person__role">Managing Director</p>
  </div>
  <ul class="contacts">
    <li><svg viewBox="0 0 14 14"><circle cx="7" cy="7" r="7" fill="var(--white)"/><path d="M4.5,3.5 l1.5,0 l0.6,2 l-1,0.8 a5,5 0 0 0 2.2,2.2 l0.8,-1 l2,0.6 l0,1.5 a6.5,6.5 0 0 1 -6.1,-6.1 Z" fill="var(--blue)"/></svg>021 555 0142</li>
    <li><svg viewBox="0 0 14 14"><circle cx="7" cy="7" r="7" fill="var(--white)"/><rect x="5" y="3" width="4" height="8" rx="0.8" fill="var(--blue)"/></svg>021 555 0187</li>
    <li><svg viewBox="0 0 14 14"><circle cx="7" cy="7" r="7" fill="var(--white)"/><rect x="3.5" y="4.5" width="7" height="5" fill="var(--blue)"/><path d="M3.5,4.5 L7,7.5 L10.5,4.5" stroke="var(--white)" stroke-width="0.8" fill="none"/></svg>info@tavenorix.com</li>
    <li><svg viewBox="0 0 14 14"><circle cx="7" cy="7" r="7" fill="var(--white)"/><circle cx="7" cy="7" r="3.5" fill="none" stroke="var(--blue)" stroke-width="1"/><path d="M3.5,7 H10.5 M7,3.5 V10.5" stroke="var(--blue)" stroke-width="0.8"/></svg>www.tavenorix.com</li>
    <li><svg viewBox="0 0 14 14"><circle cx="7" cy="7" r="7" fill="var(--white)"/><path d="M7,11 C5,8.5 4.5,7.2 4.5,6 a2.5,2.5 0 0 1 5,0 C9.5,7.2 9,8.5 7,11 Z" fill="var(--blue)"/></svg>14 Crystal Park Road, Suite 5</li>
  </ul>
</section>

</body>
</html>
```